Business Card for my New Brokerage

Looking to get a business card design for my new Real Estate Brokerage.
I want it with Picture, Phone Number, Email, Website, Office Address
Name and Designation. Please add logo too.

Target Market(s)

Real Estate Investors or Home Buyers

Industry/Entity Type

Real Estate

Contact Information for Business Card

Name, Email, Phone Number, website, email, office address

Colors
EB3D1F
EC4F4E
F09395
F8D3D4
FCEDEE

Requirements
Must have
• Minimalistic, Clean, Modern, Photo
Nice to have
• White and Red Colors

```html
<!DOCTYPE html>
<html lang="en">
<head>
<meta charset="utf-8">
<title>Ember Realty Inc – Business Card</title>
<link rel="stylesheet" href="https://fonts.googleapis.com/css2?family=Montserrat:wght@400;500;700&display=swap">
<style>
  :root {
    --red: #e03a1f;
    --ink: #2b2b2b;
    --paper: #ffffff;
    --stage: #d3d6d8;
    --skyline-top: rgba(236, 237, 238, 0);
    --skyline-bottom: #e6e7e8;
    --photo-light: #c9b6a6;
    --photo-dark: #3d4450;
  }
  * { box-sizing: border-box; margin: 0; padding: 0; }
  html, body {
    width: 1187px; height: 1200px; overflow: hidden;
    background: var(--stage);
    font-family: "Montserrat", sans-serif;
  }
  .card {
    position: absolute;
    background: var(--paper);
    overflow: hidden;
  }
  .card--front { left: 217px; top: 121px; width: 753px; height: 430px; }
  .card--back  { left: 213px; top: 643px; width: 762px; height: 435px; }

  .skyline {
    position: absolute; right: 0; bottom: 0;
    background: linear-gradient(to bottom, var(--skyline-top) 0%, var(--skyline-bottom) 35%, var(--skyline-bottom) 100%);
  }
  .card--front .skyline { left: 0; top: 253px; }
  .card--back .skyline  { left: 150px; top: 246px; }

  .brand {
    position: absolute; left: 0; right: 0; top: 178px;
    text-align: center; color: var(--red); font-weight: 700;
    z-index: 1;
  }
  .brand__name { font-size: 82px; line-height: 1; letter-spacing: 1px; }
  .brand__sub  { font-size: 24px; letter-spacing: 6px; margin-top: 8px; padding-left: 30px; }

  .front-web {
    position: absolute; left: 0; right: 0; top: 382px;
    text-align: center; color: #fff; font-size: 15px; letter-spacing: 2px;
    z-index: 1;
  }

  .portrait {
    position: absolute; left: 0; top: 0; width: 190px; height: 100%;
    background: linear-gradient(to bottom, var(--photo-light) 0%, var(--photo-light) 45%, var(--photo-dark) 70%, var(--photo-dark) 100%);
    z-index: 1;
  }

  .agent {
    position: absolute; right: 49px; top: 50px; text-align: right; z-index: 1;
  }
  .agent__name  { color: var(--red); font-weight: 700; font-size: 30px; letter-spacing: 1px; line-height: 1.1; }
  .agent__title { color: var(--ink); font-size: 17px; letter-spacing: 1px; margin-top: 6px; }

  .address {
    position: absolute; right: 49px; top: 255px; text-align: right;
    color: var(--ink); font-size: 17px; letter-spacing: 0.8px; line-height: 28px; z-index: 1;
  }
  .contacts {
    position: absolute; right: 49px; top: 320px; list-style: none;
    color: var(--ink); font-size: 17px; letter-spacing: 0.8px; z-index: 1;
  }
  .contacts li {
    display: flex; justify-content: flex-end; align-items: center; gap: 12px;
    height: 29px;
  }
  .contacts svg { width: 14px; height: 14px; fill: var(--red); flex: none; }
</style>
</head>
<body>

<section class="card card--front">
  <div class="skyline" role="img" aria-label="Faint grey city skyline illustration"></div>
  <div class="brand">
    <div class="brand__name">EMBER</div>
    <div class="brand__sub">REALTY INC</div>
  </div>
  <div class="front-web">www.emberrealtyinc.com</div>
</section>

<section class="card card--back">
  <div class="skyline" role="img" aria-label="Faint grey city skyline illustration"></div>
  <div class="portrait" role="img" aria-label="Portrait photo of the broker in a grey suit and blue tie"></div>

  <div class="agent">
    <div class="agent__name">MARCUS HALE</div>
    <div class="agent__title">Broker Associate</div>
  </div>

  <address class="address" style="font-style:normal">
    214 216, Harborview Complex<br>
    Westfield Business Park
  </address>

  <ul class="contacts">
    <li>401-555-0148
      <svg viewBox="0 0 16 16" aria-hidden="true"><path d="M12.5 10.2l-2 1.3c-.4.2-.9.1-1.2-.2L5.6 7.3c-.3-.4-.3-.9 0-1.2L7 4.2 4.6.8 2 2.4C.6 4.8 3.5 10 7 13c2.9 2.4 5.2 3.1 6.8 1.7l1.5-2.2z"/></svg>
    </li>
    <li>info@emberrealtyinc.com
      <svg viewBox="0 0 16 16" aria-hidden="true"><path d="M0 3h16v10H0z" fill="var(--red)"/><path d="M0 3.5l8 5.5 8-5.5M0 13l6-5M16 13l-6-5" stroke="#fff" stroke-width="1.2" fill="none"/></svg>
    </li>
    <li>www.emberrealtyinc.com
      <svg viewBox="0 0 16 16" aria-hidden="true"><circle cx="8" cy="8" r="7.5"/><g stroke="#fff" stroke-width="1" fill="none"><ellipse cx="8" cy="8" rx="3" ry="7"/><path d="M1 8h14M2 4.5h12M2 11.5h12M8 1v14"/></g></svg>
    </li>
  </ul>
</section>

</body>
</html>
```